Box and label design for oil Tincture bottle

I need to design an attractive looking label for a 30ml CBD oil tincture along with designing a box for the tincture oil. I already have the logo (see attachment). I just need a nice, attractive looking artwork for the label and the box. The box is the standard 30ml tincture oil (see example attachment). The box has a total of 6 sides (4 on sides and 2 for top and bottom). Please include a section for supplemental facts and ingredients. Let's not focus to much on content. I am more concerned with design of box and label.
Target Market(s)
CBD customers
Look and feel
Each slider illustrates characteristics of the customer's brand and the style your logo design should communicate.

```html
<!DOCTYPE html>
<html lang="en">
<head>
<meta charset="utf-8">
<title>Bright Harbor CBD – Tincture Box and Label</title>
<link rel="stylesheet" href="https://fonts.googleapis.com/css2?family=Oswald:wght@500&family=Roboto:wght@500;700&family=Roboto+Condensed:wght@400;700&display=swap">
<style>
  :root {
    --canvas: #f4f4f4;
    --panel: #ededed;
    --panel-shade: #9d9d9d;
    --brand-blue: #2f3fd8;
    --navy: #2d3878;
    --ink: #1a1a1a;
    --rule: #5a6ee0;
    --art-red: #c8203a;
    --art-pink: #e23f86;
    --art-purple: #7a2bb0;
    --art-teal: #1fa6c4;
    --art-orange: #ef7a1a;
    --art-blue: #2a3fb8;
  }
  * { box-sizing: border-box; margin: 0; padding: 0; }
  html, body { width: 1200px; height: 989px; overflow: hidden; }
  body {
    background: var(--canvas);
    font-family: "Roboto", Arial, sans-serif;
    color: var(--ink);
    position: relative;
  }

  .panel {
    position: absolute;
    background: var(--panel);
    border: 1px solid #d6d6d6;
  }

  /* Box side panel */
  .box-side {
    left: 150px; top: 215px; width: 230px; height: 560px;
    background: linear-gradient(180deg, #a8a8a8, var(--panel-shade));
  }
  .directions {
    position: absolute; left: 16px; right: 16px; top: 120px;
    border: 1px solid #555; border-radius: 8px;
    padding: 26px 14px 14px;
  }
  .directions-title {
    position: absolute; top: -11px; left: 50%; transform: translateX(-50%);
    background: #555; color: #eee; font-size: 12px;
    padding: 3px 10px; border-radius: 4px;
    font-family: "Roboto Condensed", Arial, sans-serif;
  }
  .directions-text {
    font-family: "Roboto Condensed", Arial, sans-serif;
    font-size: 9.5px; line-height: 1.55; color: #222; text-align: center;
  }
  .web-address {
    position: absolute; left: 0; right: 0; bottom: 24px;
    text-align: center; font-family: "Roboto Condensed", Arial, sans-serif;
    font-weight: 700; font-size: 14px; color: #222;
  }

  /* Box front panel */
  .box-front {
    left: 380px; top: 215px; width: 300px; height: 560px;
    background: linear-gradient(180deg, #f3f3f3, #e4e4e4);
  }

  .brand {
    position: absolute; left: 0; right: 0; text-align: center;
  }
  .brand-mark {
    display: block; margin: 0 auto 10px;
    border-radius: 50%; background: var(--brand-blue);
  }
  .brand-name {
    font-family: "Oswald", Arial, sans-serif; font-weight: 500;
    color: var(--brand-blue); letter-spacing: 0.5px; line-height: 1.05;
  }
  .brand-rule { height: 1px; background: var(--rule); margin: 6px auto 0; }

  .product-title { position: absolute; left: 0; right: 0; text-align: center; }
  .product-kicker {
    font-family: "Roboto", Arial, sans-serif; font-weight: 500;
    color: var(--navy); letter-spacing: 3px;
  }
  .product-name {
    font-family: "Roboto", Arial, sans-serif; font-weight: 700;
    color: var(--ink); line-height: 1.05;
  }

  .art-burst {
    position: absolute;
    background:
      linear-gradient(135deg, var(--art-orange) 0%, var(--art-red) 25%, var(--art-pink) 45%, var(--art-purple) 65%, var(--art-teal) 82%, var(--art-blue) 100%);
    clip-path: polygon(30% 0, 100% 0, 70% 100%, 0 100%);
    opacity: 0.9;
  }

  .contents { position: absolute; text-align: center; font-family: "Roboto Condensed", Arial, sans-serif; }
  .contents-volume { color: var(--navy); font-weight: 700; }
  .contents-strength { color: var(--ink); font-weight: 700; }

  /* Front sizes */
  .box-front .brand { top: 80px; }
  .box-front .brand-mark { width: 56px; height: 56px; }
  .box-front .brand-name { font-size: 24px; }
  .box-front .brand-rule { width: 150px; }
  .box-front .product-title { top: 222px; }
  .box-front .product-kicker { font-size: 20px; margin-bottom: 4px; }
  .box-front .product-name { font-size: 34px; }
  .box-front .art-burst { left: 20px; top: 340px; width: 170px; height: 180px; }
  .box-front .contents { right: 26px; bottom: 30px; }
  .box-front .contents-volume { font-size: 22px; }
  .box-front .contents-strength { font-size: 22px; }

  /* Bottle label */
  .bottle-label {
    left: 760px; top: 330px; width: 260px; height: 330px;
    background: linear-gradient(180deg, #f0f0f0, #e2e2e2);
  }
  .bottle-label .brand { top: 28px; }
  .bottle-label .brand-mark { width: 40px; height: 40px; margin-bottom: 8px; }
  .bottle-label .brand-name { font-size: 18px; }
  .bottle-label .brand-rule { width: 112px; }
  .bottle-label .product-title { top: 140px; }
  .bottle-label .product-kicker { font-size: 15px; margin-bottom: 2px; }
  .bottle-label .product-name { font-size: 25px; }
  .bottle-label .art-burst { left: 0; top: 170px; width: 60px; height: 110px; }
  .bottle-label .contents { left: 0; right: 0; bottom: 30px; }
  .bottle-label .contents-volume { font-size: 17px; }
  .bottle-label .contents-strength { font-size: 16px; }
</style>
</head>
<body>

  <section class="panel box-side" aria-label="Box side panel">
    <div class="directions">
      <span class="directions-title">Directions</span>
      <p class="directions-text">Shake well before use. Fill dropper to the marked line and place oil under the tongue. Hold for sixty seconds, then swallow. Start with half a dropper once daily and adjust as needed. Store in a cool, dry place away from light. Keep out of reach of children. Consult your doctor before use if pregnant or nursing.</p>
    </div>
    <p class="web-address">www.BrightHarborCBD.com</p>
  </section>

  <section class="panel box-front" aria-label="Box front panel">
    <div class="brand">
      <span class="brand-mark"></span>
      <p class="brand-name">BRIGHT HARBOR CBD</p>
      <div class="brand-rule"></div>
    </div>
    <div class="product-title">
      <p class="product-kicker">ALL NATURAL</p>
      <p class="product-name">CANNABIS<br>TINCTURE</p>
    </div>
    <div class="art-burst" role="img" aria-label="Colourful abstract geometric burst of angled blocks in red, pink, purple, orange, teal and blue"></div>
    <div class="contents">
      <p class="contents-volume">30 mL</p>
      <p class="contents-strength">CBD: 300 mg</p>
    </div>
  </section>

  <section class="panel bottle-label" aria-label="Bottle label">
    <div class="brand">
      <span class="brand-mark"></span>
      <p class="brand-name">BRIGHT HARBOR CBD</p>
      <div class="brand-rule"></div>
    </div>
    <div class="product-title">
      <p class="product-kicker">ALL NATURAL</p>
      <p class="product-name">CANNABIS<br>TINCTURE</p>
    </div>
    <div class="art-burst" role="img" aria-label="Colourful abstract geometric burst of angled blocks in red, pink, purple, teal and blue"></div>
    <div class="contents">
      <p class="contents-volume">30 mL</p>
      <p class="contents-strength">CBD: 300 mg</p>
    </div>
  </section>

</body>
</html>
```